New design for PeopleDesk

We are at the start of the process of evolving an existing business, and have just developed a new logo that will guide the look and feel of the rest of the site.

PeopleDesk.com.au will be the place to go for small business owners that need guidance and tools on how to look after HR functions such as recruitment and performance management amongst other aspects.

The existing site that is going to be evolved in www.hiringcornerfolk.com.au - while some of the content will remain, the entire look of the site needs to change, and a new homepage and other pages need to be developed.

For this project, we'd like the new homepage to be designed to lead the way for how the rest of the pages will look moving forward.

We're looking for a clean, clear and modern design. It should not feel cluttered or busy

The wireframe for the new homepage, and another landing page are attached.

Target Market(s)

Small and medium business owners - slightly male skew

Industry/Entity Type

Small Business

Requirements
Must have
• - Should be clean and simple
- The overall feel from the new logo (attached to the project) should be integrated into all elements of the site
- Should communicate that the site is easy to navigate
- Should communicate that the site is friendly and approachable
- Should communicate that the site is professional (for small businesses)
Nice to have
• This homepage for this site is quite a good design reference in terms of clean design.

http://www.choremoose.com/

For PeopleDesk though, the 3 boxes under the main image should appear above the fold though.

Also, happy for one other colour to be introduced to highlight call to action buttons etc.
Should not have
• Must not be cluttered
Should not introduce more than one additional colour to the existing colours from the logo

```html
<!DOCTYPE html>
<html lang="en">
<head>
<meta charset="utf-8">
<title>PeopleDesk – Home</title>
<link href="https://fonts.googleapis.com/css2?family=Arimo:wght@400;700&display=swap" rel="stylesheet">
<style>
  :root {
    --brand-blue: #1a6fb5;
    --sky-blue: #2b95dd;
    --text-grey: #666666;
    --heading-grey: #7a7a7a;
    --body-grey: #555555;
    --nav-top: #8a8a8c;
    --nav-bottom: #4f5053;
    --nav-active-top: #b9b9ba;
    --nav-active-bottom: #8c8c8e;
    --hero-edge: #c6cbd4;
    --card-top: #ffffff;
    --card-bottom: #d8d8d8;
    --rule: #c9c9c9;
    --wood-light: #f0cf9e;
    --wood-dark: #c98f55;
    --screen-light: #6fc0f2;
    --screen-dark: #2f8fd9;
    --badge-grey: #9a9a9a;
  }
  * { box-sizing: border-box; margin: 0; padding: 0; }
  html, body { width: 1200px; height: 874px; overflow: hidden; background: #ffffff; }
  body { font-family: "Arimo", Arial, sans-serif; position: relative; color: var(--body-grey); }

  .site-logo { position: absolute; left: 155px; top: 38px; display: flex; align-items: center; gap: 8px; }
  .site-logo .logo-dot { width: 30px; height: 30px; border-radius: 50%; background: var(--brand-blue); }
  .site-logo .logo-name { font-size: 30px; font-weight: 700; color: var(--brand-blue); letter-spacing: -0.5px; }

  .tagline { position: absolute; right: 164px; top: 50px; font-size: 19px; color: var(--text-grey); }

  .main-nav { position: absolute; left: 151px; top: 100px; width: 902px; height: 33px; border-radius: 4px;
    background: linear-gradient(var(--nav-top), var(--nav-bottom)); overflow: hidden; }
  .main-nav a { position: absolute; top: 0; height: 33px; line-height: 33px; color: #fff; font-size: 14px; text-decoration: none; }
  .main-nav .active { background: linear-gradient(var(--nav-active-top), var(--nav-active-bottom)); font-weight: 700; padding: 0 19px; }
  .main-nav .sep { position: absolute; top: 8px; width: 1px; height: 17px; background: rgba(255,255,255,0.3); }

  .hero-band { position: absolute; left: 39px; top: 140px; width: 1161px; height: 313px;
    background: radial-gradient(ellipse 45% 90% at 50% 15%, #ffffff 40%, var(--hero-edge) 100%); }
  .hero-arrow { position: absolute; top: 220px; }
  .hero-arrow.prev { left: 49px; }
  .hero-arrow.next { left: 1117px; }

  .video-frame { position: absolute; left: 386px; top: 187px; width: 425px; height: 232px; border-radius: 4px 4px 0 0;
    background: linear-gradient(#e8e8e8, #bcbcbc 14%, var(--screen-light) 14%, var(--screen-dark)); }
  .video-tray { position: absolute; left: 347px; top: 384px; width: 505px; height: 105px; border-radius: 6px 6px 14px 14px;
    background: linear-gradient(var(--wood-light), var(--wood-dark)); }
  .play-button { position: absolute; left: 571px; top: 292px; }

  .headline { position: absolute; left: 0; width: 1204px; top: 504px; text-align: center; font-size: 27px; font-weight: 700; color: var(--brand-blue); }
  .subline { position: absolute; left: 0; width: 1204px; top: 539px; text-align: center; font-size: 19px; color: var(--sky-blue); }

  .card { position: absolute; top: 574px; height: 202px; border-radius: 4px;
    background: linear-gradient(var(--card-top), var(--card-bottom)); box-shadow: 0 1px 4px rgba(0,0,0,0.35); }
  .card h2 { font-size: 24px; font-weight: 700; color: var(--heading-grey); }
  .about-card { left: 158px; width: 268px; padding: 20px 24px 0 24px; }
  .about-card p { font-size: 12.5px; line-height: 17px; text-align: justify; color: var(--body-grey); margin-top: 8px; }
  .about-card h2 + p { margin-top: 10px; }

  .news-card { left: 463px; width: 278px; padding: 15px 40px 0 20px; }
  .news-list { list-style: none; margin-top: 10px; }
  .news-list li { position: relative; padding: 5px 0 5px 21px; font-size: 12.5px; line-height: 17px; border-bottom: 1px solid var(--rule); }
  .news-list li:last-child { border-bottom: none; }
  .news-list li::before { content: ""; position: absolute; left: 2px; top: 11px; width: 10px; height: 10px;
    background: radial-gradient(circle, #9a9a9a 1.3px, transparent 1.6px) 0 0 / 3.3px 3.3px; }

  .partners-card { left: 774px; width: 254px; text-align: center; padding-top: 17px; }
  .partners-card h2 { font-size: 21px; }
  .partner-badges { position: absolute; left: 22px; top: 68px; display: flex; gap: 15px; }
  .partner-badge { width: 41px; height: 41px; border-radius: 50%; background: var(--badge-grey); }
  .partners-rule { position: absolute; left: 27px; right: 29px; top: 128px; height: 1px; background: var(--rule); }
  .social-links { position: absolute; left: 22px; top: 143px; display: flex; gap: 14px; }
  .social-links span { width: 42px; height: 41px; border-radius: 3px; box-shadow: 0 1px 2px rgba(0,0,0,0.3); }
  .social-links .s1 { background: linear-gradient(#4e71b8, #2f4f92); }
  .social-links .s2 { background: linear-gradient(#9fdcf8, #5fbfe9); }
  .social-links .s3 { background: linear-gradient(#7fcbe0, #4ca9c8); }
  .social-links .s4 { background: linear-gradient(#3ea3e6, #1373c2); }

  .site-footer { position: absolute; left: 168px; top: 805px; width: 858px; border-top: 1px solid var(--rule); }
  .site-footer a { position: absolute; top: 15px; font-size: 12.5px; color: var(--body-grey); text-decoration: none; white-space: nowrap; }
</style>
</head>
<body>
  <header>
    <div class="site-logo"><span class="logo-dot"></span><span class="logo-name">PeopleDesk</span></div>
    <p class="tagline">Lorem Ipsum is simply dummy text of the printing</p>
    <nav class="main-nav">
      <a style="left:25px">Attract</a>
      <span class="sep" style="left:81px"></span>
      <a style="left:97px">Recruit</a>
      <a class="active" style="left:162px">Induction</a>
      <a style="left:282px">Engage</a>
      <span class="sep" style="left:347px"></span>
      <a style="left:366px">Performance Management</a>
      <span class="sep" style="left:549px"></span>
      <a style="left:568px">Termination &amp; Redundancy</a>
      <span class="sep" style="left:758px"></span>
      <a style="left:777px">Community</a>
    </nav>
  </header>

  <section class="hero">
    <div class="hero-band"></div>
    <svg class="hero-arrow prev" width="36" height="98" viewBox="0 0 36 98"><polyline points="35,1 2,49 35,97" fill="none" stroke="#8c8c8c" stroke-width="2"/></svg>
    <svg class="hero-arrow next" width="36" height="98" viewBox="0 0 36 98"><polyline points="1,1 34,49 1,97" fill="none" stroke="#8c8c8c" stroke-width="2"/></svg>
    <div class="video-frame" role="img" aria-label="Browser window showing an introductory video with a presenter on a blue backdrop"></div>
    <div class="video-tray" role="img" aria-label="Wooden tray holding the video window"></div>
    <svg class="play-button" width="54" height="54" viewBox="0 0 54 54"><circle cx="27" cy="27" r="24.5" fill="none" stroke="#fff" stroke-width="3"/><polygon points="21,15 39,27 21,39" fill="#fff"/></svg>
    <h1 class="headline">Australia’s leading provider of educational tools that enable</h1>
    <p class="subline">a successful DIY recruitment process</p>
  </section>

  <main>
    <article class="card about-card">
      <h2>About us</h2>
      <p>Lorem Ipsum is simply dummy text of the printing and typesetting industry. Lorem Ipsum has been the industry's standard dummy text ever since the 1500s</p>
      <p>when an unknown printer took a galley of type and scrambled</p>
    </article>
    <article class="card news-card">
      <h2>News/community</h2>
      <ul class="news-list">
        <li>Lorem Ipsum is simply dummy text of the printing</li>
        <li>Typesetting industry. Lorem Ipsum has been the industry's</li>
        <li>Typesetting industry. Lorem Ipsum has been the industry's</li>
      </ul>
    </article>
    <article class="card partners-card">
      <h2>Partners</h2>
      <div class="partner-badges"><span class="partner-badge"></span><span class="partner-badge"></span><span class="partner-badge"></span><span class="partner-badge"></span></div>
      <div class="partners-rule"></div>
      <div class="social-links"><span class="s1"></span><span class="s2"></span><span class="s3"></span><span class="s4"></span></div>
    </article>
  </main>

  <footer class="site-footer">
    <a style="left:17px">© 2012Privacy Policy</a>
    <a style="left:156px">Terms &amp; Conditions</a>
    <a style="left:291px">Sitemap</a>
    <a style="left:364px">Contact</a>
    <a style="left:431px">Lost your files?</a>
    <a style="left:534px">Your Feedback</a>
  </footer>
</body>
</html>
```